Cannabis Vape Cartridge Box. For HUGE Cannabis brand.

We need help with a product for our All-in-One Rosin Vape product. Our brand is called Torvaq, and we are based in New Mexico. The product is all natural so we want the design look like natural as well. We will be using a soft touch box, so we want the packaging to look how the box feels in the hands. The box feels soft and smooth. We do not want to use any cannabis leaves in the design. We are also interested in vibrational patterns. I have attached examples of packaging that we like as well as the template of our boxes we will be using and also our logos.
Updates
With all new designs- please put the word Rosin on the box.
Colors
Designer to choose colors to be used in the design.
Look and feel

```html
<!DOCTYPE html>
<html lang="en">
<head>
<meta charset="utf-8">
<title>Torvaq Rosin Disposable Vape – Box Dieline</title>
<link href="https://fonts.googleapis.com/css2?family=Bebas+Neue&family=Roboto+Condensed:wght@400;700&display=swap" rel="stylesheet">
<style>
  :root {
    --backdrop: #afcbbb;
    --mint: #74c3b0;
    --sage: #d7e3c3;
    --teal-deep: #2f6e73;
    --slate: #4f5f7e;
    --rose: #e2607a;
    --cream: #eef3e6;
    --ink: #141414;
    --warning-red: #e0222b;
    --fold: rgba(255, 255, 255, 0.55);
  }
  html, body {
    margin: 0;
    width: 1200px;
    height: 900px;
    overflow: hidden;
    background: var(--backdrop);
  }
  .dieline { display: block; width: 1200px; height: 900px; }
  .flap-top { fill: var(--mint); }
  .flap-bottom { fill: var(--sage); }
  .fold-line { stroke: var(--fold); stroke-width: 2; fill: none; }
  .info-panel { fill: var(--cream); }
  .info-heading { font-family: "Bebas Neue", sans-serif; font-size: 22px; fill: var(--ink); }
  .info-text, .info-text tspan { font-family: "Roboto Condensed", sans-serif; font-size: 14px; fill: var(--ink); font-weight: 400; }
  .info-text tspan.strong { font-weight: 700; }
  .brand-name { font-family: "Bebas Neue", sans-serif; font-size: 108px; fill: var(--ink); }
  .brand-name-small { font-family: "Bebas Neue", sans-serif; font-size: 40px; fill: var(--ink); }
  .brand-seal { fill: var(--cream); }
  .product-label { fill: var(--cream); }
  .product-label-text { font-family: "Bebas Neue", sans-serif; font-size: 21px; fill: var(--ink); }
  .product-label-rule { stroke: var(--ink); stroke-width: 1.5; }
  .net-weight { font-family: "Bebas Neue", sans-serif; font-size: 21px; fill: var(--ink); }
  .warning-diamond { fill: #ffffff; stroke: var(--warning-red); stroke-width: 8; stroke-linejoin: round; }
  .warning-text { font-family: "Roboto Condensed", sans-serif; font-weight: 700; fill: var(--warning-red); }
</style>
</head>
<body>
<svg class="dieline" viewBox="640 40 2080 1560" xmlns="http://www.w3.org/2000/svg">
  <defs>
    <linearGradient id="flowing-swirl" x1="0" y1="0" x2="1" y2="1">
      <stop offset="0" stop-color="#74c3b0"/>
      <stop offset="0.22" stop-color="#2f6e73"/>
      <stop offset="0.38" stop-color="#8fcfba"/>
      <stop offset="0.52" stop-color="#e2607a"/>
      <stop offset="0.64" stop-color="#4f5f7e"/>
      <stop offset="0.8" stop-color="#d7e3c3"/>
      <stop offset="1" stop-color="#74c3b0"/>
    </linearGradient>
  </defs>

  <!-- top flaps -->
  <path class="flap-top" d="M1750 345 V180 H1768 Q1772 80 1805 80 H1880 Q1908 80 1912 180 H1915 V345 Z"/>
  <path class="flap-top" d="M1590 345 V300 L1635 212 H1750 V345 Z"/>
  <path class="flap-top" d="M1915 345 V212 H2030 L2072 320 V345 Z"/>
  <text class="brand-name-small" x="1832" y="285" text-anchor="middle">Torvaq</text>

  <!-- bottom flaps -->
  <path class="flap-bottom" d="M1422 1295 V1460 Q1422 1555 1480 1555 H1528 Q1585 1555 1585 1460 V1295 Z"/>
  <path class="flap-bottom" d="M1585 1295 V1425 H1750 V1295 Z"/>
  <path class="flap-bottom" d="M1915 1295 V1425 H2072 V1295 Z"/>

  <!-- box body with flowing marbled artwork -->
  <path d="M1282 365 L1425 345 V1295 L1282 1278 Z" fill="url(#flowing-swirl)" role="img" aria-label="Flowing marbled swirl artwork in mint, teal, rose and sage"/>
  <rect x="1425" y="345" width="647" height="950" fill="url(#flowing-swirl)" role="img" aria-label="Flowing marbled swirl artwork in mint, teal, rose and sage"/>

  <!-- fold lines -->
  <path class="fold-line" d="M1425 345 V1295 M1585 345 V1295 M1750 345 V1295 M1915 345 V1295 M1425 345 H2072 M1425 1295 H2072"/>

  <!-- back panel: compliance information -->
  <rect class="info-panel" x="1425" y="362" width="157" height="918"/>
  <text class="info-heading" x="1432" y="390" textLength="140" lengthAdjust="spacingAndGlyphs">Must be 21+ to enjoy</text>
  <text class="info-text" x="1432">
    <tspan x="1432" y="412" class="strong">WARNING: For use by</tspan>
    <tspan x="1432" dy="16.7" class="strong">adults 21 and over.</tspan><tspan> Keep</tspan>
    <tspan x="1432" dy="16.7">out of reach of children.</tspan>
    <tspan x="1432" dy="16.7">Do not drive or operate</tspan>
    <tspan x="1432" dy="16.7">heavy machinery while</tspan>
    <tspan x="1432" dy="16.7">under the influence of</tspan>
    <tspan x="1432" dy="16.7">cannabis. BE CAUTIOUS a</tspan>
    <tspan x="1432" dy="16.7" class="strong">Cannabinoid edibles can</tspan>
    <tspan x="1432" dy="16.7" class="strong">take up to two hours or</tspan>
    <tspan x="1432" dy="16.7" class="strong">more to take effect.</tspan><tspan> This</tspan>
    <tspan x="1432" dy="16.7">product is not approved</tspan>
    <tspan x="1432" dy="16.7">by the FDA to treat, cure,</tspan>
    <tspan x="1432" dy="16.7">or prevent any disease.</tspan>
    <tspan x="1432" dy="16.7">FDA has not evaluated</tspan>
    <tspan x="1432" dy="16.7">this product for safety,</tspan>
    <tspan x="1432" dy="16.7">effectiveness, and quality.</tspan>
    <tspan x="1432" dy="16.7">There may be long term.</tspan>
    <tspan x="1432" dy="16.7">adverse health effects</tspan>
    <tspan x="1432" dy="16.7">from consumption of</tspan>
    <tspan x="1432" dy="16.7">cannabis, including</tspan>
    <tspan x="1432" dy="16.7">additional risks for</tspan>
    <tspan x="1432" dy="16.7">women who are or may</tspan>
    <tspan x="1432" dy="16.7">become pregnant or are</tspan>
    <tspan x="1432" dy="16.7">breastfeeding. For</tspan>
    <tspan x="1432" dy="16.7">accidental Ingestion: Call</tspan>
    <tspan x="1432" dy="16.7">Poison Control</tspan>
    <tspan x="1432" dy="16.7">1-800-555-0142</tspan>
    <tspan x="1432" y="877" class="strong">INGREDIENTS:</tspan>
    <tspan x="1432" dy="16.7">Ethanol extracted</tspan>
    <tspan x="1432" dy="16.7">Cannabis oil, natural</tspan>
    <tspan x="1432" dy="16.7">terpenes</tspan>
    <tspan x="1432" y="956" class="strong">No pesticides used in the</tspan>
    <tspan x="1432" dy="16.7" class="strong">making of this product.</tspan>
    <tspan x="1432" y="1001" class="strong">Solvents used:</tspan><tspan> Ethanol</tspan>
    <tspan x="1432" y="1154" class="strong">Expires one year after</tspan>
    <tspan x="1432" dy="16.7" class="strong">manufacturing date.</tspan>
    <tspan x="1432" y="1219" class="strong">Intended use:</tspan><tspan> Inhalant</tspan>
    <tspan x="1432" y="1247" class="strong">DIRECTIONS:</tspan><tspan> Press to lips</tspan>
    <tspan x="1432" dy="16.7">and inhale</tspan>
  </text>

  <!-- front panel: brand and product -->
  <circle class="brand-seal" cx="1912" cy="535" r="158"/>
  <text class="brand-name" text-anchor="middle">
    <tspan x="1808" y="545">T</tspan>
    <tspan x="1808" y="645">O</tspan>
    <tspan x="1808" y="745">R</tspan>
    <tspan x="1808" y="845">V</tspan>
    <tspan x="1808" y="945">A</tspan>
    <tspan x="1808" y="1045">Q</tspan>
  </text>

  <polygon class="warning-diamond" points="1993,1045 2045,1097 1993,1149 1941,1097"/>
  <text class="warning-text" x="1993" y="1080" text-anchor="middle" font-size="26">!</text>
  <text class="warning-text" x="1993" y="1107" text-anchor="middle" font-size="22">THC</text>

  <rect class="product-label" x="1758" y="1118" width="150" height="88" rx="5"/>
  <text class="product-label-text" x="1833" y="1144" text-anchor="middle">Carefully Blended</text>
  <text class="product-label-text" x="1833" y="1166" text-anchor="middle">Disposable Vape</text>
  <line class="product-label-rule" x1="1766" y1="1175" x2="1900" y2="1175"/>
  <text class="product-label-text" x="1833" y="1198" text-anchor="middle" letter-spacing="2">Rosin</text>
  <text class="net-weight" x="1833" y="1252" text-anchor="middle">1 Gram</text>
</svg>
</body>
</html>
```